QuillaVorn needs a dashboard page designed

Redesign the dashboard shown in the provided images.

There are two images:
- dashboard.png
- dashboard-expanded.png

NOTE: The vocabulary navigation on the left will be a very long list of words 100s, so keep that in mind when you're designing both the vocab navigation and the expanded vocab popup.

In the dashboard.png picture, there needs to be a progress chart showing the word progress like the following: review 1(show it as completed) -> review 2(show the user they are here) -> review 3(unvisited) -> review 4(unvisited)

The do-not-design-this-page.png image is for your reference only. It is not to be designed. Use it to understand the overall look and feel of the website to help you create the best dashboard page possible.
Updates

Need extra days to review

Industry/Entity Type

Education English learning

Number of Pages Required

1 page

Requirements
Must have
• The main navigation and main header cannot change between pages. See the do-not-design page for the main navigateion and header.
Should not have
• Do not add a person profile. We will not have images of our users. Keep the icons in the main navigation as they are.

```html
<!DOCTYPE html>
<html lang="en">
<head>
<meta charset="utf-8">
<title>QuillaVorn – WordPath Tutor Dashboard</title>
<link href="https://fonts.googleapis.com/css2?family=Poppins:wght@400;500;600;700&family=Roboto:wght@400;500&display=swap" rel="stylesheet">
<style>
  :root {
    --navy: #262d37;
    --navy-deep: #1b2028;
    --orange: #f08a00;
    --orange-bright: #f5b400;
    --orange-deep: #e24a00;
    --ink: #1f1f1f;
    --panel: #f5f5f5;
    --white: #ffffff;
    --band-long: #effce9;
    --band-working: #eaf3fd;
    --band-short: #fdf4ea;
    --band-forgot: #eefbe9;
    --dot: #a9a9a9;
  }
  * { box-sizing: border-box; margin: 0; padding: 0; }
  html, body { width: 1200px; height: 1051px; overflow: hidden; }
  body { position: relative; background: var(--navy); font-family: "Roboto", sans-serif; color: var(--ink); }

  .brand { position: absolute; left: 0; top: 40px; width: 207px; text-align: center;
    font-family: "Poppins", sans-serif; font-weight: 700; font-size: 20px; color: var(--white); }
  .brand-dot { display: block; width: 22px; height: 22px; border-radius: 50%; background: var(--orange); margin: 0 auto 6px; }

  .topbar-title { position: absolute; left: 646px; top: 15px; font-family: "Poppins", sans-serif;
    font-weight: 600; font-size: 16px; color: var(--white); display: flex; align-items: center; gap: 3px; }
  .topbar-actions { position: absolute; left: 1000px; top: 10px; display: flex; align-items: center; gap: 0; }
  .avatar { position: absolute; left: 1084px; top: 10px; width: 32px; height: 32px; border-radius: 50%;
    background: linear-gradient(135deg, #c98a5a, #6b4a36); border: 2px solid var(--orange); }

  .vocab-nav { position: absolute; left: 8px; top: 114px; width: 183px; height: 261px; background: var(--navy-deep); border-radius: 12px; }
  .vocab-nav .nav-home { position: absolute; left: 21px; top: 18px; }
  .vocab-nav .nav-heading { position: absolute; left: 23px; top: 66px; font-weight: 500; font-size: 15px; color: var(--orange); }
  .vocab-list { list-style: none; position: absolute; left: 3px; top: 112px; width: 174px; }
  .vocab-list li { height: 30px; line-height: 30px; padding-left: 20px; font-size: 15px; color: var(--white); margin-bottom: 4.5px; }
  .vocab-list li.is-active { background: var(--orange); border-radius: 15px; font-weight: 500; }

  .section-link { position: absolute; left: 31px; color: var(--white); font-size: 15px; }
  .section-link svg { display: block; margin-bottom: 8px; }

  .main { position: absolute; left: 207px; top: 55px; width: 993px; height: 996px; background: var(--panel); border-top-left-radius: 38px; }
  .abs { position: absolute; }

  .step-label { position: absolute; top: 101px; width: 120px; margin-left: -60px; text-align: center; font-weight: 500; font-size: 15px; color: var(--ink); }
  .step-label.is-done { color: var(--orange); }

  .word-title { position: absolute; left: 0; width: 1010px; top: 149px; text-align: center; font-family: "Poppins", sans-serif; font-weight: 700; font-size: 40px; color: var(--orange); }
  .pill { position: absolute; left: 352px; width: 289px; height: 35px; border-radius: 18px; background: var(--orange);
    color: var(--white); font-family: "Poppins", sans-serif; font-weight: 600; font-size: 12.5px;
    display: flex; align-items: center; justify-content: center; gap: 8px; }
  .copy { position: absolute; left: 90px; width: 820px; text-align: center; font-family: "Poppins", sans-serif; font-size: 13.5px; line-height: 19px; color: var(--ink); }

  .curve-frame { position: absolute; left: 78px; top: 390px; width: 838px; height: 382px; border: 4px solid var(--orange); border-radius: 31px; background: var(--white); }
  .curve-chart { position: absolute; left: 78px; top: 390px; }
</style>
</head>
<body>
  <div class="brand"><span class="brand-dot"></span>QuillaVorn</div>

  <div class="topbar-title">WordPath Tutor
    <svg width="22" height="22" viewBox="0 0 22 22"><circle cx="11" cy="11" r="11" fill="#f08a00"/><path d="M6.5 9h9l-4.5 5z" fill="#fff"/></svg>
  </div>
  <div class="topbar-actions">
    <svg width="22" height="22" viewBox="0 0 24 24" style="margin-right:16px"><path fill="#fff" d="M19.4 13a7.5 7.5 0 0 0 0-2l2.1-1.6-2-3.5-2.5 1a7.6 7.6 0 0 0-1.7-1L15 3h-4l-.4 2.9a7.6 7.6 0 0 0-1.7 1l-2.5-1-2 3.5L6.6 11a7.5 7.5 0 0 0 0 2l-2.1 1.6 2 3.5 2.5-1a7.6 7.6 0 0 0 1.7 1L11 21h4l.4-2.9a7.6 7.6 0 0 0 1.7-1l2.5 1 2-3.5zM13 15.5a3.5 3.5 0 1 1 0-7 3.5 3.5 0 0 1 0 7z" transform="translate(-1 0)"/></svg>
    <svg width="30" height="30" viewBox="0 0 30 30"><path fill="#fff" d="M10 11a5 5 0 0 1 10 0v5l2 3H8l2-3zM13 20h4a2 2 0 0 1-4 0z"/><circle cx="23" cy="8" r="7" fill="#f08a00"/><text x="23" y="11" text-anchor="middle" font-family="Roboto, sans-serif" font-size="9" fill="#fff">0</text></svg>
  </div>
  <div class="avatar" role="img" aria-label="User profile photo"></div>
  <svg class="abs" style="left:1118px;top:22px" width="10" height="8" viewBox="0 0 10 8"><path d="M0 1h10L5 7z" fill="#fff"/></svg>

  <nav class="vocab-nav">
    <svg class="nav-home" width="33" height="31" viewBox="0 0 33 31"><path d="M16.5 2 1 16l3 3 2-1.8V30h8v-8h5v8h8V17.2l2 1.8 3-3L26 6.5V2h-4v1z" fill="#f08a00"/></svg>
    <div class="nav-heading">WordPath Tutor</div>
    <ul class="vocab-list">
      <li>Short-Term Memory</li>
      <li class="is-active">Grab</li>
      <li>Working Memory</li>
      <li>Long-Term Memory</li>
    </ul>
  </nav>

  <div class="section-link" style="top:438px">
    <svg width="33" height="34" viewBox="0 0 33 34"><path d="M16.5 2a8 8 0 0 0-8 8c0 6 8 14 8 14s8-8 8-14a8 8 0 0 0-8-8zm0 11a3 3 0 1 1 0-6 3 3 0 0 1 0 6z" fill="#fff"/><path d="M1 32 6 22h5l5.5 6 5.5-6h5l5 10z" fill="#fff"/></svg>
    Daily English
  </div>
  <div class="section-link" style="top:583px">
    <svg width="30" height="34" viewBox="0 0 30 34"><path d="M4 33V14h8V6h10V1h3v32zM7 17v3h2v-3zm0 6v3h2v-3zm8-14v3h2V9zm0 6v3h2v-3zm0 6v3h2v-3zm5-12v3h2V9zm0 6v3h2v-3zm0 6v3h2v-3z" fill="#fff" fill-rule="evenodd"/></svg>
    Business
  </div>

  <main class="main">
    <svg class="abs" style="left:0;top:0" width="993" height="100" viewBox="0 0 993 100">
      <line x1="207" y1="72.5" x2="371" y2="72.5" stroke="#f08a00" stroke-width="2.5"/>
      <line x1="415" y1="72.5" x2="579" y2="72.5" stroke="#262d37" stroke-width="2.5"/>
      <line x1="623" y1="72.5" x2="787" y2="72.5" stroke="#262d37" stroke-width="2.5"/>
      <circle cx="185.5" cy="72.5" r="21" fill="#fff" stroke="#f08a00" stroke-width="2.5"/>
      <circle cx="393" cy="72.5" r="21" fill="#fff" stroke="#262d37" stroke-width="2.5"/>
      <path d="M393 51.5a21 21 0 0 0 0 42" fill="none" stroke="#f08a00" stroke-width="2.5"/>
      <circle cx="601" cy="72.5" r="21" fill="#fff" stroke="#262d37" stroke-width="2.5"/>
      <circle cx="809" cy="72.5" r="21" fill="#fff" stroke="#262d37" stroke-width="2.5"/>
      <g fill="none" stroke="#f08a00" stroke-width="2.5" stroke-linecap="round" stroke-linejoin="round">
        <path d="M180.5 72.5l3.5 3.5 6.5-7"/><path d="M388 72.5l3.5 3.5 6.5-7"/>
        <path d="M596 72.5l3.5 3.5 6.5-7"/><path d="M804 72.5l3.5 3.5 6.5-7"/>
      </g>
    </svg>
    <div class="step-label is-done" style="left:185.5px">Review 1</div>
    <div class="step-label" style="left:393px">Review 2</div>
    <div class="step-label" style="left:601px">Review 3</div>
    <div class="step-label" style="left:809px">Review 4</div>

    <h1 class="word-title" style="left:-14px;width:1000px">Grab</h1>
    <div class="pill" style="top:215px">
      <svg width="10" height="11" viewBox="0 0 10 11"><path d="M0 0l10 5.5L0 11z" fill="#fff"/></svg>
      Start Vocabulary Review Exercise 3
    </div>
    <p class="copy" style="top:269px">The word "grab" is most commonly used as averb, meaning to take something quickly or suddenly. Imagine you're running late for school. You don't have time for breakfast, so you quickly grab an apple from the kitchen and rush out the door. As you reach the bus stop, your friend waves and says, "Hey! Let's grab a coffee after class." Later, when you sit down, your phone starts ringing. You grab it from your bag and answer.</p>

    <div class="curve-frame"></div>
    <svg class="curve-chart" width="838" height="382" viewBox="0 0 838 382" font-family="Poppins, sans-serif">
      <defs>
        <linearGradient id="barFill" x1="0" y1="0" x2="0" y2="1">
          <stop offset="0" stop-color="#f5b400"/><stop offset="1" stop-color="#e24a00"/>
        </linearGradient>
      </defs>
      <rect x="41" y="60" width="769" height="66" fill="#effce9"/>
      <rect x="41" y="126" width="769" height="140" fill="#eaf3fd"/>
      <rect x="41" y="266" width="769" height="28" fill="#fdf4ea"/>
      <rect x="41" y="294" width="769" height="30" fill="#eefbe9"/>
      <g font-size="13.5" fill="#1f1f1f" text-anchor="end">
        <text x="782" y="84">Long-Term Memory</text>
        <text x="782" y="149">Working Memory</text>
        <text x="782" y="289">Short-Term Memory</text>
        <text x="782" y="316">Forgotten Memory</text>
      </g>
      <path d="M93 324V277a14.7 14.7 0 0 1 29.4 0V324z" fill="url(#barFill)"/>
      <path d="M174 324V108a14.7 14.7 0 0 1 29.4 0V324z" fill="url(#barFill)"/>
      <path d="M110 310q46 20 50 58" transform="translate(0 -44)" fill="none" stroke="#333" stroke-width="0.8" stroke-dasharray="2 2"/>
      <path d="M202 146C290 148 330 220 336 321" transform="translate(0 -8)" fill="none" stroke="#222" stroke-width="1.2" stroke-dasharray="4 3"/>
      <g fill="#a9a9a9">
        <circle cx="46" cy="324" r="5"/><circle cx="129" cy="324" r="5"/><circle cx="211" cy="324" r="5"/>
        <circle cx="294" cy="324" r="5"/><circle cx="376" cy="324" r="5"/><circle cx="458" cy="324" r="5"/>
        <circle cx="541" cy="324" r="5"/><circle cx="623" cy="324" r="5"/><circle cx="706" cy="324" r="5"/>
        <circle cx="788" cy="324" r="5"/>
      </g>
      <g font-size="13.5" fill="#1f1f1f" text-anchor="middle">
        <text x="46" y="347">18 May</text><text x="129" y="347">19 May</text><text x="211" y="347">20 May</text>
        <text x="294" y="347">21 May</text><text x="376" y="347">22 May</text><text x="458" y="347">23 May</text>
        <text x="541" y="347">24 May</text><text x="623" y="347">25 May</text><text x="706" y="347">26 May</text>
        <text x="788" y="347">27 May</text>
      </g>
      <g font-size="8.5" fill="#1f1f1f" text-anchor="middle">
        <circle cx="107.5" cy="288" r="18" fill="#fff" stroke="#eee"/>
        <text x="107.5" y="286">May</text><text x="107.5" y="297">18</text>
        <circle cx="189" cy="119" r="18" fill="#fff" stroke="#eee"/>
        <text x="189" y="117">May</text><text x="189" y="128">18</text>
      </g>
    </svg>
    <div class="pill" style="top:374px">Learning Curve Graph</div>

    <div class="pill" style="top:807px">WordPath Tutor Learning Analysis</div>
    <p class="copy" style="top:865px;left:80px;width:840px">Lorem ipsum dolor sit amet, consectetur adipiscing elit, sed do eiusmod tempor incididunt ut labore et dolore magna aliqua. Ut enim ad minim veniam, quis nostrud exercitation ullamco laboris nisi ut aliquip ex ea commodo consequat. Duis aute irure dolor in reprehenderit in voluptate velit esse cillum dolore eu fugiat nulla pariatur. Excepteur sint occaecat cupidatat non proident, sunt in culpa qui officia deserunt mollit anim id est laborum.</p>
  </main>
</body>
</html>
```